Direct Mail Postcard- Lighting Company

Our task is to send a postcard directly to houses surrounding where our company has done work. My goal is to position ourselves as the go to outdoor lighting partner for their neighborhood.
Trusted Lighting Design & Maintenance Your neighbor chose us to enhance and maintain their home's beauty and security. Now, we're offering our top-tier services to the entire neighborhood.
Please emphasize our:
Maintenance Excellence:
Regular system check-ups
Prompt repair and replacement
Upgrades to the latest technology
Less emphasis on:
Our Services:
High-Quality Landscape & Architectural Lighting
Reliable Permanent Lighting Solutions
Call us today and take advantage of our 25% discount (limited time offer)
For more details or to schedule a consultation, visit brightvane-mo.com or call .
*Need to be able to tweak this for future campaigns. Quickly edit verbiage for future marketing campaigns. I.e. a file that can be edited through Canva
*Inspiration photo file (Yard Glow Horizons)
*Would like to incorporate the before and after png
Call: (816) 555-0193
brightvane-mo.com
Updates
I attached a new before and after photo. Please create a design implementing this
Look and feel
Each slider illustrates characteristics of the customer's brand and the style your logo design should communicate.

```html
<!DOCTYPE html>
<html lang="en">
<head>
<meta charset="utf-8">
<title>Brightvane Lighting – Neighborhood Postcard</title>
<link href="https://fonts.googleapis.com/css2?family=Poppins:wght@400;600;700;800&family=Great+Vibes&family=Dela+Gothic+One&display=swap" rel="stylesheet">
<style>
  :root {
    --page: #e9e9e9;
    --ink: #050505;
    --white: #ffffff;
    --gold: #c9a862;
    --gold-light: #e6cf8f;
    --gold-dark: #9c7a3a;
    --bulb: #f3dd8a;
  }
  * { box-sizing: border-box; margin: 0; padding: 0; }
  html, body { width: 1200px; height: 897px; overflow: hidden; background: var(--page); }
  .postcard {
    position: absolute; left: 0; top: 40px; width: 1200px; height: 817px;
    background: var(--ink); overflow: hidden; font-family: "Poppins", sans-serif; color: var(--white);
  }
  .hero-photo {
    position: absolute; left: 300px; top: 0; width: 900px; height: 817px;
    background:
      radial-gradient(ellipse 140px 150px at 500px 300px, rgba(214,120,50,.85), transparent 70%),
      radial-gradient(ellipse 260px 300px at 780px 200px, rgba(190,140,50,.55), transparent 70%),
      radial-gradient(ellipse 500px 320px at 520px 180px, #1f3a1c, transparent 75%),
      linear-gradient(180deg, #233a22 0%, #1a2a18 45%, #0e1a0e 70%, #050805 100%);
  }
  .hero-fade {
    position: absolute; left: 0; top: 0; width: 1200px; height: 817px;
    background:
      linear-gradient(90deg, var(--ink) 0%, var(--ink) 30%, rgba(5,5,5,.75) 45%, rgba(5,5,5,0) 62%),
      linear-gradient(0deg, var(--ink) 0%, var(--ink) 17%, rgba(5,5,5,0) 40%);
  }
  .brand { position: absolute; left: 60px; top: 72px; font-size: 34px; font-weight: 600; color: var(--gold); line-height: 1; }
  .headline { position: absolute; left: 60px; top: 158px; font-size: 30px; font-weight: 800; line-height: 40px; }
  .headline-with { position: absolute; left: 58px; top: 238px; font-family: "Great Vibes", cursive; font-size: 50px; color: var(--gold); }
  .headline-premium { position: absolute; left: 58px; top: 262px; font-size: 76px; font-weight: 800; line-height: 1; letter-spacing: -1px; }
  .headline-lighting {
    position: absolute; left: 58px; top: 336px; font-size: 76px; font-weight: 800; line-height: 1; letter-spacing: -1px;
    background: linear-gradient(180deg, var(--gold-light), var(--gold-dark)); -webkit-background-clip: text; background-clip: text; color: transparent;
  }
  .bulb-line { position: absolute; left: 48px; top: 412px; }
  .trust-title { position: absolute; left: 82px; top: 424px; font-size: 17px; font-weight: 700; line-height: 21px; }
  .trust-copy { position: absolute; left: 86px; top: 471px; font-size: 18.5px; line-height: 22px; }
  .trust-copy span { color: var(--gold); }
  .offer-pill {
    position: absolute; left: 58px; top: 559px; width: 553px; height: 70px; border-radius: 35px;
    background: linear-gradient(90deg, #a98745, #d9bd7a 45%, #a78643 75%, #cdb26f);
    padding: 9px 0 0 28px; font-size: 18px; line-height: 23px;
  }
  .offer-pill strong { font-weight: 700; }
  .cta { position: absolute; left: 57px; top: 652px; }
  .cta-title { font-size: 20px; font-weight: 600; line-height: 24px; }
  .cta-sub { font-size: 15px; color: var(--gold); line-height: 20px; }
  .cta-tag { margin-top: 5px; width: 242px; height: 25px; border-radius: 13px; background: var(--gold); color: var(--white); font-size: 12.5px; font-weight: 700; text-align: center; line-height: 26px; }
  .cta-rules { margin-top: 6px; width: 242px; height: 36px; background: repeating-linear-gradient(180deg, var(--gold) 0 1px, transparent 1px 6px); }
  .discount { position: absolute; left: 318px; top: 640px; }
  .discount-figure { font-family: "Dela Gothic One", sans-serif; font-size: 86px; line-height: 86px; letter-spacing: -2px; }
  .discount-figure small { font-size: 46px; color: var(--gold); letter-spacing: 0; }
  .discount-word { font-family: "Dela Gothic One", sans-serif; font-size: 24px; line-height: 28px; color: var(--gold); letter-spacing: 6px; margin-top: 0; }
  .discount-note { font-size: 16px; letter-spacing: 3px; margin-top: 2px; }
  .divider { position: absolute; left: 609px; top: 648px; width: 1px; height: 125px; background: #6c6c6c; }
  .snapshot { position: absolute; width: 212px; height: 212px; background: var(--white); padding: 8px; box-shadow: 0 4px 12px rgba(0,0,0,.5); }
  .snapshot-photo { width: 100%; height: 100%; position: relative; overflow: hidden; }
  .snapshot-label { position: absolute; left: 0; bottom: 0; width: 92px; height: 28px; background: var(--gold); clip-path: polygon(0 0, 82% 0, 100% 100%, 0 100%); font-size: 17px; font-weight: 600; line-height: 28px; padding-left: 12px; }
  .snapshot-before { left: 680px; top: 448px; transform: rotate(-2deg); }
  .snapshot-before .snapshot-photo { background: linear-gradient(160deg, #1b1b1a, #0a0a0a 60%, #12160f); }
  .snapshot-after { left: 902px; top: 451px; transform: rotate(3deg); }
  .snapshot-after .snapshot-photo { background: radial-gradient(ellipse 90px 70px at 120px 90px, #bdb3a4, #4a463f 70%, #101010), linear-gradient(180deg, #0d1118, #1a2416); }
  .contact-lead { position: absolute; left: 669px; top: 705px; font-size: 18px; line-height: 22px; }
  .contact-lead span { display: block; color: var(--gold); font-weight: 700; }
  .contact-phone { position: absolute; left: 800px; top: 697px; display: flex; align-items: center; gap: 9px; font-size: 37px; font-weight: 700; }
  .contact-web { position: absolute; left: 801px; top: 747px; font-size: 26px; font-weight: 700; }
</style>
</head>
<body>
  <main class="postcard">
    <div class="hero-photo" role="img" aria-label="Two-storey brick house at dusk with warm landscape uplighting on the facade and a large tree"></div>
    <div class="hero-fade"></div>

    <p class="brand">Brightvane Lighting</p>

    <h1>
      <span class="headline">Elevate Your<br>Outdoor Spaces</span>
      <span class="headline-with">with</span>
      <span class="headline-premium">PREMIUM</span>
      <span class="headline-lighting">LIGHTING</span>
    </h1>

    <svg class="bulb-line" width="40" height="140" viewBox="0 0 40 140" aria-hidden="true">
      <defs>
        <radialGradient id="bulbGlow">
          <stop offset="0" stop-color="#f3dd8a" stop-opacity=".9"/>
          <stop offset="1" stop-color="#f3dd8a" stop-opacity="0"/>
        </radialGradient>
      </defs>
      <line x1="18" y1="0" x2="18" y2="95" stroke="#c9a862" stroke-width="1.5"/>
      <circle cx="18" cy="112" r="20" fill="url(#bulbGlow)"/>
      <rect x="14" y="94" width="8" height="6" fill="#c9a862"/>
      <circle cx="18" cy="110" r="11" fill="#f3dd8a"/>
    </svg>

    <p class="trust-title">Trusted Lighting Design<br>&amp; Maintenance</p>
    <p class="trust-copy">Your neighbor chose us to enhance<br>&nbsp;and maintain their <span>home's beauty</span><br>&nbsp;&nbsp;<span>and security</span></p>

    <p class="offer-pill">Now, we're offering<br><strong>our top-tier services to the entire neighborhood</strong></p>

    <div class="cta">
      <p class="cta-title">REACH OUT TODAY TO</p>
      <p class="cta-sub">SCHEDULE YOUR APPOINTMENT</p>
      <p class="cta-tag">AND TAKE ADVANTAGE OF OUR</p>
      <div class="cta-rules"></div>
    </div>

    <div class="discount">
      <p class="discount-figure">25<small>%</small></p>
      <p class="discount-word">DISCOUNT</p>
      <p class="discount-note">LIMITED TIME OFFER</p>
    </div>

    <div class="divider"></div>

    <figure class="snapshot snapshot-before">
      <div class="snapshot-photo" role="img" aria-label="Before: house at night with no outdoor lighting">
        <span class="snapshot-label">Before</span>
      </div>
    </figure>
    <figure class="snapshot snapshot-after">
      <div class="snapshot-photo" role="img" aria-label="After: same house at night with landscape lighting installed">
        <span class="snapshot-label">After</span>
      </div>
    </figure>

    <p class="contact-lead">SPEAK WITH<span>A LIGHTING<br>DESIGNER</span></p>
    <p class="contact-phone">
      <svg width="40" height="40" viewBox="0 0 40 40" aria-hidden="true">
        <circle cx="20" cy="20" r="19" fill="#c9a862"/>
        <path d="M13 11c1-1 2.5-1 3.2.2l2 3.2c.6 1 .3 2-.5 2.7l-1.2 1c1 2.3 2.8 4.2 5.2 5.3l1-1.2c.7-.8 1.8-1 2.7-.4l3.2 2c1.1.7 1.2 2.2.2 3.2l-1.6 1.6c-1.4 1.4-3.6 1.6-5.4.7-4.8-2.4-8.4-6-10.7-10.8-.9-1.8-.6-4 .8-5.4z" fill="#050505"/>
      </svg>
      (816) 555-0193
    </p>
    <p class="contact-web">www.brightvane-mo.com</p>
  </main>
</body>
</html>
```